Insurance Flyers

Design one sided insurance card flyer. Use the wording i have in the word file. green cab pictures can be different. you can google " green taxi nyc" or "vbk taxi new york"

Insurance

```html
<!DOCTYPE html>
<html lang="en">
<head>
<meta charset="utf-8">
<title>Northway Insurance – Green Car VBK Insurance Flyer</title>
<link rel="stylesheet" href="https://fonts.googleapis.com/css2?family=Open+Sans:wght@600;700&family=Philosopher:ital,wght@1,700&family=Teko:wght@300;400;500&display=swap">
<style>
  :root {
    --navy: #23337f;
    --pill-top: #3f86cc;
    --pill-bottom: #1b4f91;
    --lime: #8cc63f;
    --teal: #4bbcc8;
    --ink: #111111;
    --grey-text: #505050;
    --tick: #2a63b0;
    --cab: #b5d58b;
    --cab-shade: #98bd6c;
    --art-warm: #e6b08a;
    --art-blue: #5d86c9;
    --page: #ffffff;
  }
  * { box-sizing: border-box; margin: 0; padding: 0; }
  html, body { width: 1200px; height: 1000px; overflow: hidden; background: var(--page); }
  .canvas { position: relative; width: 1200px; height: 1000px; }

  .flyer {
    position: absolute; left: 293px; top: 104px; width: 613px; height: 792px; overflow: hidden;
    background: linear-gradient(180deg, #e3f1c4 0%, #f8fcef 22%, #ffffff 40%, #ffffff 70%, #f2f9e2 86%, #dcefb5 100%);
    font-family: "Open Sans", Arial, sans-serif;
  }
  .flyer .deco { position: absolute; inset: 0; width: 613px; height: 792px; }

  .brand {
    position: absolute; top: 40px; left: 0; width: 100%; text-align: center;
    font-family: "Open Sans", Arial, sans-serif; font-weight: 700; font-size: 52px;
    color: var(--navy); letter-spacing: -1px; line-height: 1.3;
  }
  .address-line {
    position: absolute; top: 141px; left: 0; width: 100%; text-align: center;
    font-size: 13px; font-weight: 700; color: var(--ink); white-space: nowrap;
  }
  .services-pill {
    position: absolute; top: 164px; left: 35px; width: 544px; height: 27px; border-radius: 14px;
    background: linear-gradient(180deg, var(--pill-top), var(--pill-bottom));
    color: #fff; font-size: 11.5px; font-weight: 700; text-align: center; line-height: 27px;
    white-space: nowrap; box-shadow: 0 2px 3px rgba(0,0,0,.25);
  }
  .headline {
    position: absolute; top: 208px; left: 0; width: 100%; text-align: center;
    font-family: "Philosopher", Georgia, serif; font-style: italic; font-weight: 700;
    font-size: 33px; color: var(--lime); line-height: 1.15;
  }
  .headline .tagline { display: block; font-size: 30px; }

  .benefits { position: absolute; top: 294px; left: 30px; list-style: none; }
  .benefits li {
    font-family: "Teko", "Arial Narrow", sans-serif; font-weight: 300; font-size: 17px;
    color: var(--grey-text); text-transform: uppercase; height: 19.3px; line-height: 19.3px;
    display: flex; align-items: center; gap: 12px; white-space: nowrap;
  }
  .benefits svg { width: 13px; height: 13px; flex: none; }
  .promise {
    position: absolute; top: 453px; left: 32px; width: 270px;
    font-family: "Teko", "Arial Narrow", sans-serif; font-weight: 300; font-size: 17px; line-height: 19px;
    color: var(--grey-text); text-transform: uppercase;
  }

  .fleet { position: absolute; left: 319px; top: 296px; width: 280px; height: 340px; }
  .vehicle { position: absolute; left: 0; width: 280px; }
  .vehicle .tag {
    position: absolute; left: 0; top: 0; padding: 0 10px; height: 20px; line-height: 20px;
    border-radius: 10px; background: linear-gradient(180deg, var(--pill-top), var(--pill-bottom));
    color: #fff; font-family: Georgia, serif; font-weight: 700; font-size: 9.5px; text-transform: uppercase;
  }
  .vehicle .photo {
    position: absolute; left: 48px; border-radius: 30px 40px 8px 8px;
    background: linear-gradient(180deg, var(--cab) 0%, var(--cab-shade) 100%);
  }
  .v-sedan { top: 4px; } .v-sedan .photo { top: 6px; width: 200px; height: 58px; }
  .v-town { top: 78px; } .v-town .photo { top: 4px; width: 228px; height: 68px; left: 40px; }
  .v-minivan { top: 166px; } .v-minivan .photo { top: -6px; width: 202px; height: 76px; }
  .v-suv { top: 246px; } .v-suv .photo { top: -2px; width: 194px; height: 80px; }

  .service-box {
    position: absolute; left: 19px; top: 504px; width: 286px; height: 153px;
    border: 3px solid var(--teal); border-radius: 14px; background: #fff;
    box-shadow: 2px 2px 4px rgba(0,0,0,.25);
  }
  .service-box .art {
    position: absolute; left: 14px; top: 10px; width: 252px; height: 90px; border-radius: 10px;
    background: linear-gradient(90deg, var(--art-warm) 0%, #f3dcc8 40%, #e46a5a 62%, var(--art-blue) 100%);
  }
  .service-box .caption {
    position: absolute; left: 0; top: 108px; width: 100%; text-align: center;
    font-family: "Teko", "Arial Narrow", sans-serif; font-weight: 500; font-size: 22px;
    color: var(--navy); text-transform: uppercase; letter-spacing: 0; line-height: 26px;
    white-space: nowrap;
  }

  .divider {
    position: absolute; left: 25px; top: 666px; width: 568px; height: 3px;
    background: linear-gradient(90deg, rgba(35,51,127,0) 0%, var(--navy) 20%, var(--navy) 80%, rgba(35,51,127,0) 100%);
  }
  .contact {
    position: absolute; top: 680px; left: 0; width: 100%; text-align: center;
    font-size: 12.5px; font-weight: 700; color: var(--ink); line-height: 17px; white-space: nowrap;
  }
</style>
</head>
<body>
<div class="canvas">
  <section class="flyer">
    <svg class="deco" viewBox="0 0 613 792" aria-hidden="true">
      <polygon points="560,0 613,0 613,30" fill="#a7d13a"/>
      <polygon points="430,0 613,0 613,110" fill="#eaf5cf" opacity=".7"/>
      <polygon points="0,0 180,0 0,140" fill="#d9ecb4" opacity=".5"/>
      <polygon points="613,640 613,792 430,792" fill="#b9dc5c" opacity=".55"/>
      <polygon points="613,700 613,792 520,792" fill="#a1cc2f"/>
      <polygon points="0,640 0,792 190,792" fill="#e4f1c6" opacity=".7"/>
    </svg>

    <div class="brand">Northway Insurance</div>
    <p class="address-line">418 5th Ave Queens NY 11375 | Tel:718-555-0142 - Fax:718-555-0198</p>
    <div class="services-pill">TAXI AND LIMOUSINE PROFESSIONALS, BLACK CAR, CAR SERVICE, LIVERY AND AMBULETTTES</div>

    <h1 class="headline">GREEN CAR VBK INSURANCE<span class="tagline">“Your one stop shop”</span></h1>

    <ul class="benefits">
      <li><svg viewBox="0 0 14 14"><path d="M1.5 7.5l3.5 3.5L12.5 2.5" fill="none" stroke="var(--tick)" stroke-width="2.6" stroke-linecap="round" stroke-linejoin="round"/></svg>Flexible payment plans</li>
      <li><svg viewBox="0 0 14 14"><path d="M1.5 7.5l3.5 3.5L12.5 2.5" fill="none" stroke="var(--tick)" stroke-width="2.6" stroke-linecap="round" stroke-linejoin="round"/></svg>Liability and full coverage</li>
      <li><svg viewBox="0 0 14 14"><path d="M1.5 7.5l3.5 3.5L12.5 2.5" fill="none" stroke="var(--tick)" stroke-width="2.6" stroke-linecap="round" stroke-linejoin="round"/></svg>Corporations, individuals and wheelchair accessible</li>
      <li><svg viewBox="0 0 14 14"><path d="M1.5 7.5l3.5 3.5L12.5 2.5" fill="none" stroke="var(--tick)" stroke-width="2.6" stroke-linecap="round" stroke-linejoin="round"/></svg>DMV &amp; TLC services</li>
      <li><svg viewBox="0 0 14 14"><path d="M1.5 7.5l3.5 3.5L12.5 2.5" fill="none" stroke="var(--tick)" stroke-width="2.6" stroke-linecap="round" stroke-linejoin="round"/></svg>Six hour defensive driving course</li>
      <li><svg viewBox="0 0 14 14"><path d="M1.5 7.5l3.5 3.5L12.5 2.5" fill="none" stroke="var(--tick)" stroke-width="2.6" stroke-linecap="round" stroke-linejoin="round"/></svg>Claim handeling</li>
      <li><svg viewBox="0 0 14 14"><path d="M1.5 7.5l3.5 3.5L12.5 2.5" fill="none" stroke="var(--tick)" stroke-width="2.6" stroke-linecap="round" stroke-linejoin="round"/></svg>Workers compensation</li>
      <li><svg viewBox="0 0 14 14"><path d="M1.5 7.5l3.5 3.5L12.5 2.5" fill="none" stroke="var(--tick)" stroke-width="2.6" stroke-linecap="round" stroke-linejoin="round"/></svg>Same day insurance cards</li>
    </ul>
    <p class="promise">We know this is your livelihood and want to help you get on the road as quick as possible</p>

    <div class="fleet">
      <div class="vehicle v-sedan"><div class="photo" role="img" aria-label="Photo of a green taxi sedan, side view"></div><span class="tag">Sedan</span></div>
      <div class="vehicle v-town"><div class="photo" role="img" aria-label="Photo of a green taxi town car, side view"></div><span class="tag">Town Car</span></div>
      <div class="vehicle v-minivan"><div class="photo" role="img" aria-label="Photo of a green taxi minivan, side view"></div><span class="tag">Minivan</span></div>
      <div class="vehicle v-suv"><div class="photo" role="img" aria-label="Photo of a green taxi SUV, side view"></div><span class="tag">SUV</span></div>
    </div>

    <div class="service-box">
      <div class="art" role="img" aria-label="Cartoon illustration of a car wash sign and a red car on a lift with a mechanic underneath"></div>
      <p class="caption">Onsite repair shop and car wash</p>
    </div>

    <div class="divider"></div>
    <div class="contact">
      Call us at 718-555-0142 or visit our office at 418 5th Ave Queens NY 11375<br>
      We are located on 5th Ave between 14th ST and 15th ST<br>
      Monday-Friday 9am till 5pm<br>
      Ask for Laura Diaz<br>
      Email: Laura@northwayinsurance.com
    </div>
  </section>
</div>
</body>
</html>
```